Business card design for Plumbing and Gas fitting company

We need a business card design for our plumbing and gas fitting company using the company logo and director details. Design should be modern and eye-catching however kept reasonably simple. This design should be targeted at commercial businesses/work so professionalism is key.

Target Market(s)

Commercial/business

Industry/Entity Type

Plumbing

Contact Information for Business Card

Warren Dohey
Director
027 581 9043
warren@vantorplumbingandgas.example
PO Box 7816
Palmerston North 4472

Font styles to use
Sans Serif

Requirements
Must have
• Logo
• Modern
• Kept simple
Nice to have
• Colour scheme based around logo

```html
<!DOCTYPE html>
<html lang="en">
<head>
<meta charset="utf-8">
<title>Vantor Plumbing &amp; Gas — Business Card</title>
<link rel="stylesheet" href="https://fonts.googleapis.com/css2?family=Ubuntu:wght@400;500;700&display=swap">
<style>
  :root {
    --bg: #ece8e2;
    --card-white: #ffffff;
    --brand-blue: #2282fb;
    --brand-blue-soft: #3b8ff5;
    --brand-orange: #ea6119;
    --ink: #1d1d1f;
    --shadow: rgba(0, 0, 0, 0.18);
  }
  * { box-sizing: border-box; margin: 0; padding: 0; }
  html, body {
    width: 1200px;
    height: 960px;
    overflow: hidden;
    background: var(--bg);
    font-family: "Ubuntu", sans-serif;
  }
  .canvas { position: relative; width: 1200px; height: 960px; }

  .card {
    position: absolute;
    width: 500px;
    height: 300px;
    box-shadow: 0 6px 18px var(--shadow);
    overflow: hidden;
  }

  /* Front */
  .card--front { left: 580px; top: 110px; background: var(--card-white); }
  .brand {
    position: absolute;
    display: flex;
    align-items: center;
    gap: 10px;
    font-weight: 700;
    white-space: nowrap;
  }
  .brand__dot { border-radius: 50%; background: var(--brand-orange); flex: none; }
  .card--front .brand { left: 34px; top: 34px; font-size: 26px; color: var(--brand-blue); }
  .card--front .brand__dot { width: 22px; height: 22px; }

  .person { position: absolute; left: 34px; top: 118px; }
  .person__name {
    font-size: 27px; font-weight: 700; color: var(--brand-blue);
    text-transform: uppercase; letter-spacing: 0.5px;
  }
  .person__role { font-size: 24px; font-weight: 700; color: var(--brand-orange); margin-top: 2px; }

  .contact { position: absolute; left: 34px; top: 200px; list-style: none; font-size: 11.5px; color: var(--ink); }
  .contact li { display: flex; align-items: flex-start; gap: 8px; margin-bottom: 9px; line-height: 1.35; }
  .contact svg { width: 11px; height: 11px; flex: none; margin-top: 2px; fill: var(--brand-blue); }

  .accent-circle {
    position: absolute; right: -40px; top: 50px;
    width: 230px; height: 230px; border-radius: 50%;
    background: var(--brand-blue); opacity: 0.12;
  }

  /* Back */
  .card--back { left: 100px; top: 500px; background: var(--brand-blue); }
  .card--back .brand {
    left: 50%; top: 50%; transform: translate(-50%, -50%);
    font-size: 32px; color: var(--card-white);
  }
  .card--back .brand__dot { width: 26px; height: 26px; }
</style>
</head>
<body>
<main class="canvas">

  <section class="card card--front" aria-label="Business card front">
    <div class="accent-circle"></div>
    <div class="brand"><span>Vantor Plumbing &amp; Gas</span><span class="brand__dot"></span></div>

    <div class="person">
      <p class="person__name">Warren Dohey</p>
      <p class="person__role">Director</p>
    </div>

    <ul class="contact">
      <li>
        <svg viewBox="0 0 24 24"><path d="M6.6 10.8a15.1 15.1 0 0 0 6.6 6.6l2.2-2.2a1 1 0 0 1 1-.25 11.4 11.4 0 0 0 3.6.57 1 1 0 0 1 1 1V20a1 1 0 0 1-1 1A17 17 0 0 1 3 4a1 1 0 0 1 1-1h3.5a1 1 0 0 1 1 1c0 1.25.2 2.45.57 3.57a1 1 0 0 1-.25 1z"/></svg>
        <span>027 581 9043</span>
      </li>
      <li>
        <svg viewBox="0 0 24 24"><path d="M2 5h20v14H2z M2 5l10 8 10-8" fill="none" stroke="#2282fb" stroke-width="2.5"/></svg>
        <span>warren@vantorplumbingandgas.example</span>
      </li>
      <li>
        <svg viewBox="0 0 24 24"><path d="M12 2a7 7 0 0 0-7 7c0 5 7 13 7 13s7-8 7-13a7 7 0 0 0-7-7zm0 9.5A2.5 2.5 0 1 1 12 6.5a2.5 2.5 0 0 1 0 5z"/></svg>
        <span>PO Box 7816<br>Palmerston North 4472</span>
      </li>
    </ul>
  </section>

  <section class="card card--back" aria-label="Business card back">
    <div class="brand"><span>Vantor Plumbing &amp; Gas</span><span class="brand__dot"></span></div>
  </section>

</main>
</body>
</html>
```